Brightwater Kinetics (formerly qzt7)

I'm doing a totally different business card now! I recently made some adjustments to my companies moving forward due to outstanding events. Because of this I will be increasing the prize money to the winner and second place.

Here is my new concept.

Brightwater Kinetics
Empowering futures.

My company will be in the following areas:
marketing & innovation, leadership & communication, energy & technology, culture & community, luxury & living.

I do not have a logo - so that is a must! Be creative and you will be rewarded!

I am looking for edgy, big, professional, dynamic!

One idea I had for the logo is a Brightwater symbol (needs to be created) and the shadow of words that describe my business (see above) behind it on one side and then the information on the other.

Go big - go nuts - be creative - YOU ROCK!

Target Market(s)

Multi-billion dollar corporations, world leaders, high end investors, millionaire entrepreneurs

Industry/Entity Type

Leadership

Requirements
Must have
• Name, title, phone, email, website, space for Qr code

Nice to have
• design on front and back. Possible the logo on one side and info on the other.

```html
<!DOCTYPE html>
<html lang="en">
<head>
<meta charset="utf-8">
<title>Brightwater Kinetics Business Card</title>
<link rel="stylesheet" href="https://fonts.googleapis.com/css2?family=Open+Sans:wght@400;600&family=Questrial&display=swap">
<style>
  :root {
    --canvas-bg: #ffffff;
    --card-face: #dcdcdc;
    --card-band: #b1b1b1;
    --ink-dark: #1c1c1c;
    --ink-mid: #4a4a4a;
    --ink-label: #666666;
    --divider: #555555;
    --qr-fill: #c4c4c4;
    --qr-edge: #8a8a8a;
  }
  * { box-sizing: border-box; margin: 0; padding: 0; }
  html, body {
    width: 1200px;
    height: 900px;
    overflow: hidden;
    background: var(--canvas-bg);
  }
  .canvas {
    position: relative;
    width: 1200px;
    height: 900px;
  }
  .card {
    position: absolute;
    width: 670px;
    height: 400px;
    border-radius: 30px;
    background: var(--card-face);
    overflow: hidden;
  }

  /* Front side */
  .card--front { left: 50px; top: 40px; }
  .card--front .wordmark {
    position: absolute;
    left: 0; right: 0;
    top: 160px;
    text-align: center;
    font-family: "Open Sans", sans-serif;
    font-weight: 400;
    font-size: 52px;
    line-height: 1;
    color: var(--ink-mid);
    white-space: nowrap;
  }
  .card--front .tagline {
    position: absolute;
    left: 0; right: 0;
    top: 245px;
    text-align: center;
    font-family: "Questrial", sans-serif;
    font-size: 18px;
    color: var(--ink-mid);
  }

  /* Back side */
  .card--back { left: 480px; top: 462px; }
  .card--back .band {
    position: absolute;
    left: 0; right: 0;
    height: 56px;
    background: var(--card-band);
  }
  .band--top { top: 0; }
  .band--bottom { bottom: 0; }
  .card--back .wordmark {
    position: absolute;
    left: 40px;
    top: 110px;
    width: 260px;
    font-family: "Open Sans", sans-serif;
    font-weight: 400;
    font-size: 38px;
    line-height: 1.1;
    color: var(--ink-mid);
  }
  .qr-space {
    position: absolute;
    left: 40px;
    top: 222px;
    width: 76px;
    height: 76px;
    background: var(--qr-fill);
    border: 2px dashed var(--qr-edge);
  }
  .card--back .divider {
    position: absolute;
    left: 318px;
    top: 100px;
    width: 3px;
    height: 205px;
    background: var(--divider);
  }
  .contact {
    position: absolute;
    left: 346px;
    top: 112px;
    width: 300px;
    font-family: "Open Sans", sans-serif;
  }
  .contact__name {
    font-size: 26px;
    font-weight: 400;
    line-height: 1.2;
    color: var(--ink-dark);
  }
  .contact__title {
    font-size: 14px;
    color: var(--ink-label);
    margin: 2px 0 16px;
  }
  .contact__list { list-style: none; }
  .contact__item {
    font-size: 13px;
    line-height: 21px;
    color: var(--ink-dark);
    white-space: nowrap;
  }
  .contact__label { color: var(--ink-label); }
</style>
</head>
<body>
<main class="canvas">
  <section class="card card--front" aria-label="Card front">
    <div class="wordmark">Brightwater Kinetics</div>
    <p class="tagline">Empowering futures.</p>
  </section>

  <section class="card card--back" aria-label="Card back">
    <div class="band band--top"></div>
    <div class="band band--bottom"></div>
    <div class="wordmark">Brightwater<br>Kinetics</div>
    <div class="qr-space" role="img" aria-label="Space reserved for QR code"></div>
    <div class="divider"></div>
    <div class="contact">
      <h1 class="contact__name">Daniel Reed</h1>
      <p class="contact__title">Managing Director</p>
      <ul class="contact__list">
        <li class="contact__item"><span class="contact__label">Email:</span> daniel@brightwater.com</li>
        <li class="contact__item"><span class="contact__label">Website:</span> www.brightwater.com.au</li>
        <li class="contact__item"><span class="contact__label">Phone Number:</span> (02)4710 382</li>
        <li class="contact__item"><span class="contact__label">Mailing Address:</span> 27 Harbour Rd</li>
      </ul>
    </div>
  </section>
</main>
</body>
</html>
```